Business card for Brightpath Partners. To be printed on clear vinyl business cards. Logo in full-color with contact information. Sample reference attached. We are hoping that the clear card will allow the colorful logo to really shine. As always, we defer to your artistic vision.

Industry/Entity Type

Business

Contact Information for Business Card

I will send our contact information for the cards. Please upload a blank template and I will award the project to you and we can go from there. I have all the information on hand and ready to go!

```html
<!DOCTYPE html>
<html lang="en">
<head>
<meta charset="utf-8">
<title>Brightpath Partners — Clear Business Card</title>
<link href="https://fonts.googleapis.com/css2?family=Montserrat:wght@400;500;700&display=swap" rel="stylesheet">
<style>
  :root {
    --page-bg: #cfcfcf;
    --page-bg-deep: #b9b9b9;
    --card-clear: rgba(255, 255, 255, 0.10);
    --card-gloss: rgba(255, 255, 255, 0.22);
    --card-edge: rgba(255, 255, 255, 0.9);
    --ink-navy: #2e3a4d;
    --ink-dark: #1d1f24;
    --tone-yellow: #f2c12e;
    --tone-orange: #ee8a3c;
    --tone-red: #e8505b;
    --tone-green: #3dbf9b;
    --tone-navy: #3c4a5f;
  }
  * { box-sizing: border-box; margin: 0; padding: 0; }
  html, body {
    width: 1200px;
    height: 1000px;
    overflow: hidden;
    font-family: "Montserrat", Arial, sans-serif;
  }
  body {
    background: linear-gradient(180deg, var(--page-bg) 0%, var(--page-bg-deep) 100%);
  }
  .business-card {
    position: absolute;
    left: 150px;
    top: 243px;
    width: 900px;
    height: 514px;
    background:
      linear-gradient(135deg, var(--card-gloss) 0%, rgba(255,255,255,0) 45%, rgba(255,255,255,0.08) 100%),
      var(--card-clear);
    border: 2px solid var(--card-edge);
    box-shadow: inset 0 0 0 1px rgba(255,255,255,0.35), 0 2px 6px rgba(0,0,0,0.06);
    overflow: hidden;
  }
  .brand-mark {
    position: absolute;
    left: 196px;
    top: 38px;
    width: 86px;
    height: 86px;
    border-radius: 50%;
    background: var(--tone-red);
    opacity: 0.9;
  }
  .brand-pattern {
    position: absolute;
    left: 440px;
    top: 0;
    width: 460px;
    height: 514px;
    background: linear-gradient(120deg,
      var(--tone-yellow) 0%,
      var(--tone-orange) 25%,
      var(--tone-red) 50%,
      var(--tone-green) 72%,
      var(--tone-navy) 100%);
    opacity: 0.8;
    -webkit-mask-image: linear-gradient(90deg, transparent 0%, #000 45%);
    mask-image: linear-gradient(90deg, transparent 0%, #000 45%);
  }
  .company-name {
    position: absolute;
    left: 40px;
    top: 170px;
    font-size: 35px;
    font-weight: 400;
    letter-spacing: 3px;
    color: var(--ink-navy);
    text-transform: uppercase;
    white-space: nowrap;
  }
  .contact-person {
    position: absolute;
    left: 40px;
    top: 288px;
  }
  .person-name {
    font-size: 31px;
    font-weight: 700;
    color: var(--ink-dark);
    text-transform: uppercase;
    line-height: 1;
  }
  .person-role {
    font-size: 22px;
    font-weight: 400;
    color: var(--ink-dark);
    margin-top: 4px;
  }
  .contact-list {
    position: absolute;
    left: 40px;
    top: 365px;
    list-style: none;
  }
  .contact-item {
    display: flex;
    align-items: center;
    height: 37.5px;
    font-size: 21px;
    font-weight: 500;
    color: var(--ink-dark);
    white-space: nowrap;
  }
  .contact-icon {
    width: 25px;
    height: 25px;
    margin-right: 18px;
    fill: none;
    stroke: var(--ink-dark);
    stroke-width: 2;
  }
</style>
</head>
<body>
  <div class="business-card">
    <div class="brand-pattern" role="img" aria-label="Large colourful brand decoration in yellow, orange, red, green and navy"></div>

    <div class="brand-mark" aria-hidden="true"></div>
    <div class="company-name">Brightpath Partners</div>

    <div class="contact-person">
      <div class="person-name">Alex Reed</div>
      <div class="person-role">Owner</div>
    </div>

    <ul class="contact-list">
      <li class="contact-item">
        <svg class="contact-icon" viewBox="0 0 24 24" aria-hidden="true"><path d="M5 4h4l2 5-2.5 1.5a11 11 0 0 0 5 5L15 13l5 2v4a2 2 0 0 1-2 2A16 16 0 0 1 3 6a2 2 0 0 1 2-2z"/></svg>
        (555) 013-2468
      </li>
      <li class="contact-item">
        <svg class="contact-icon" viewBox="0 0 24 24" aria-hidden="true"><rect x="2" y="5" width="20" height="14"/><path d="M2 5l10 8 10-8"/></svg>
        alex@brightpathmail.com
      </li>
      <li class="contact-item">
        <svg class="contact-icon" viewBox="0 0 24 24" aria-hidden="true"><circle cx="12" cy="12" r="10"/><ellipse cx="12" cy="12" rx="4.5" ry="10"/><path d="M2 12h20M4 7h16M4 17h16"/></svg>
        www.brightpathpartners.com
      </li>
    </ul>
  </div>
</body>
</html>
```